Boot Camp Flyer

Outdoor Boot Camp
SAMPLE DESIGNS I LIKE UPLOADED.
Similar to this or be creative !
I need A5 and DL flyer promoting our Boot Camp program, similar to the sample design but include our details. Pink blue green black white yellow and purple colours ok

PRICE: $100
WHEN: Thursdays & Saturdays
Thursday 6pm
Saturday 9am

WHERE: Brindle Paddock

Get results all year round! 5 week boot camp only $100
Join in any time! Register your place now!

Tone Fast Boot Camp
Register now at kestrelmovement@mailbox.example or www.social.example/kestrelmovementnz
Female only. Registration essential. ALL fitness levels welcome.

Conditions
Valid from Mar 22, 2018
Expires 26th Apr, 2018
Register online. Subject to availability. Valid for new clients only. Valid for unlimited sessions per week. Boot Camps run in 5 week blocks. Non-transferable. No refunds unless required by law. No cashback. Not to be used with any other offer.

Could maybe write 5 week tone fast challenge

Target Market(s)

Female 20s-40s

Industry/Entity Type

Fitness

Colors

Designer to choose colors to be used in the design.

Requirements
Must have
• Colour
• Easy to read font
• Picture of females (target market) exercising
Nice to have
• Terms and conditions in small print down bottom.
Should not have
• Too much text

```html
<!DOCTYPE html>
<html lang="en">
<head>
<meta charset="utf-8">
<title>Tone Fast Boot Camp Flyer</title>
<link rel="stylesheet" href="https://fonts.googleapis.com/css2?family=Oswald:wght@500;700&family=Open+Sans:wght@400;600;700;800&display=swap">
<style>
  :root {
    --white: #ffffff;
    --pink: #e8317a;
    --yellow: #f7c51e;
    --green: #2f9e44;
    --green-light: #6fcf4a;
    --ink: #1d2420;
    --photo-light: #a9b7a3;
    --photo-mid: #6f7f6c;
    --photo-dark: #3e4a3f;
  }
  * { box-sizing: border-box; margin: 0; padding: 0; }
  html, body { width: 849px; height: 1200px; overflow: hidden; background: var(--ink); }
  .flyer {
    position: relative;
    width: 849px;
    height: 1200px;
    overflow: hidden;
    font-family: "Open Sans", Arial, sans-serif;
    color: var(--white);
  }
  .hero-photo {
    position: absolute; inset: 0;
    background:
      radial-gradient(ellipse at 70% 55%, rgba(200,190,175,0.55), transparent 55%),
      linear-gradient(160deg, var(--photo-light) 0%, var(--photo-mid) 45%, var(--photo-dark) 100%);
  }
  .shade {
    position: absolute; inset: 0;
    background: linear-gradient(90deg, rgba(20,26,22,0.72) 0%, rgba(20,26,22,0.45) 55%, rgba(20,26,22,0.1) 100%);
  }
  .title-frame {
    position: absolute;
    left: 300px; top: 40px;
    width: 480px; height: 152px;
    border: 5px solid var(--pink);
  }
  .title {
    position: absolute;
    left: 150px; top: 40px;
    font-family: "Oswald", Impact, sans-serif;
    font-weight: 700;
    font-size: 128px;
    line-height: 152px;
    letter-spacing: 2px;
    text-shadow: 0 3px 10px rgba(0,0,0,0.35);
  }
  .details {
    position: absolute;
    left: 140px; top: 240px;
    font-size: 28px;
    line-height: 34px;
    font-weight: 600;
  }
  .detail-row { display: flex; }
  .detail-label {
    width: 130px;
    color: var(--yellow);
    font-weight: 800;
  }
  .price-value { color: var(--white); }
  .where-row { margin-top: 30px; }
  .pitch {
    position: absolute;
    left: 42px; top: 612px;
    width: 780px;
    font-size: 24px;
    line-height: 33px;
    font-weight: 800;
  }
  .program-banner {
    position: absolute;
    left: 0; top: 690px;
    width: 480px; height: 64px;
    background: var(--green);
    padding-left: 42px;
    font-family: "Oswald", Impact, sans-serif;
    font-weight: 700;
    font-size: 40px;
    line-height: 64px;
    text-transform: uppercase;
  }
  .register {
    position: absolute;
    left: 42px; top: 780px;
    font-size: 24px;
    line-height: 36px;
    font-weight: 600;
  }
  .register-heading { color: var(--green-light); font-weight: 800; font-size: 27px; }
  .register-or { font-weight: 800; }
  .register-note strong { color: var(--pink); font-weight: 800; }
  .brand {
    position: absolute;
    left: 36px; top: 1060px;
    display: flex; align-items: center; gap: 10px;
  }
  .brand-dot { width: 34px; height: 34px; border-radius: 50%; background: var(--pink); }
  .brand-name { font-weight: 800; font-size: 20px; line-height: 22px; width: 120px; }
  .terms {
    position: absolute;
    left: 283px; top: 1040px;
    width: 500px;
    font-size: 12px;
    line-height: 15px;
  }
  .terms-heading { font-size: 22px; line-height: 30px; font-weight: 700; }
</style>
</head>
<body>
<main class="flyer">
  <div class="hero-photo" role="img" aria-label="Photo of two women stretching outdoors on a wooden deck with green trees behind"></div>
  <div class="shade"></div>

  <div class="title-frame"></div>
  <h1 class="title">BOOTCAMP</h1>

  <section class="details">
    <div class="detail-row"><span class="detail-label">PRICE:</span><span class="price-value">$100</span></div>
    <div class="detail-row"><span class="detail-label">WHEN:</span><span>Thursdays &amp; Saturdays<br>22nd March - 26th April<br>Thursday 6pm<br>Saturday 9am</span></div>
    <div class="detail-row where-row"><span class="detail-label">WHERE:</span><span>Brindle Paddock</span></div>
  </section>

  <p class="pitch">Get results all year round! 5 week boot camp only $100<br>Join in any time! Register your place now!</p>

  <h2 class="program-banner">Tone Fast Boot Camp</h2>

  <section class="register">
    <p class="register-heading">Register now at:</p>
    <p>kestrelmovement@mailbox.example</p>
    <p class="register-or">OR</p>
    <p>www.social.example/kestrelmovementnz</p>
    <p class="register-note"><strong>Female only.</strong> Registration essential. ALL<br>fitness levels welcome.</p>
  </section>

  <div class="brand">
    <span class="brand-dot"></span>
    <span class="brand-name">Kestrel Movement</span>
  </div>

  <section class="terms">
    <p class="terms-heading">Terms &amp; Conditions</p>
    <p>Valid from Mar 22, 2018<br>Expires 26th Apr, 2018<br>Register online. Subject to availability. Valid for new clients only. Valid for unlimited sessions per week. Boot Camps run in 5 week blocks. Non-transferable. No refunds unless required by law. No cashback. Not to be used with any other offer.</p>
  </section>
</main>
</body>
</html>
```